Marine Business Card

We install Lighting, Sound, Video, PA Systems to hotels, nightclubs, Restaurants, Cruise Ships.

Target Market(s)

We want to focus on the Marine or Maritime/Cruise industry. Passenger ships and cruise liners are the companies we want to appeal to

Industry/Entity Type

Business

Contact Information for Business Card

Dale Penhallow
Managing Director
Harbourne Vista Audio Marine Ltd

Requirements
Must have
• Office: 01632 960482
Mobile: 07700 900317
dale@harbournevistaaudio.co.uk
www.harbournevistaaudio.co.uk

```html
<!DOCTYPE html>
<html lang="en">
<head>
<meta charset="utf-8">
<title>Harbourne Vista Audio Marine – Business Card</title>
<link rel="stylesheet" href="https://fonts.googleapis.com/css2?family=Quicksand:wght@400;500&family=Michroma&display=swap">
<style>
  :root {
    --page: #ffffff;
    --night: #05070d;
    --deep-navy: #0b1626;
    --sky-blue: #1d3a5e;
    --sea-blue: #2a6fa8;
    --sea-light: #8cc4ec;
    --ink: #111111;
    --white: #ffffff;
    --strip-black: #050505;
    --strip-grey: #2a2a2a;
  }
  * { box-sizing: border-box; margin: 0; padding: 0; }
  html, body {
    width: 1000px; height: 1200px; overflow: hidden;
    background: var(--page);
  }
  .canvas { position: relative; width: 1000px; height: 1200px; }

  .card {
    position: absolute;
    overflow: hidden;
    box-shadow: 0 10px 28px rgba(0,0,0,0.35);
  }

  /* Front */
  .card-front {
    left: 111px; top: 62px; width: 772px; height: 509px;
    background: linear-gradient(180deg, var(--night) 0%, var(--deep-navy) 45%, var(--sky-blue) 64%, var(--night) 68%);
  }
  .sea-photo {
    position: absolute; left: 0; right: 0; bottom: 0; height: 185px;
    background:
      radial-gradient(ellipse 60% 70% at 50% 20%, rgba(200,230,255,0.55), transparent 70%),
      linear-gradient(180deg, var(--sea-light) 0%, var(--sea-blue) 45%, #123a63 100%);
  }
  .front-logo {
    position: absolute; left: 0; right: 0; top: 160px;
    text-align: center;
    font-family: "Quicksand", sans-serif; font-weight: 400;
    font-size: 76px; line-height: 1; letter-spacing: 1px;
    color: var(--white);
  }
  .front-tagline {
    position: absolute; left: 0; right: 0; top: 256px;
    text-align: center;
    font-family: "Quicksand", sans-serif; font-weight: 500;
    font-size: 30px; letter-spacing: 1px;
    color: var(--white);
  }

  /* Back */
  .card-back {
    left: 111px; top: 631px; width: 774px; height: 509px;
    background: var(--white);
    border: 1px solid #333;
  }
  .side-strip {
    position: absolute; left: 0; top: 0; bottom: 0; width: 181px;
    background: linear-gradient(90deg, var(--strip-black) 0%, var(--strip-black) 55%, var(--strip-grey) 80%, #9a9a9a 100%);
  }
  .side-logo {
    position: absolute; left: 60px; top: 265px;
    transform: translate(-50%, -50%) rotate(90deg);
    white-space: nowrap; text-align: center;
    color: var(--white);
    font-family: "Quicksand", sans-serif;
  }
  .side-logo .name { display: block; font-size: 34px; font-weight: 400; line-height: 1; }
  .side-logo .sub { display: block; font-size: 11px; font-weight: 500; margin-top: 6px; letter-spacing: 0.5px; }

  .person {
    position: absolute; right: 36px; top: 66px; text-align: right;
    font-family: "Michroma", sans-serif; color: var(--ink);
  }
  .person-name {
    font-size: 38px; line-height: 1.1;
    text-shadow: 3px 4px 5px rgba(0,0,0,0.45);
  }
  .person-role { font-size: 22px; margin-top: 2px; }

  .contact {
    position: absolute; left: 198px; top: 252px;
    font-family: "Michroma", sans-serif; color: var(--ink);
    font-size: 21px; line-height: 39.5px; list-style: none;
    white-space: nowrap;
  }
  .contact .company { text-shadow: 2px 3px 4px rgba(0,0,0,0.35); }
</style>
</head>
<body>
<div class="canvas">

  <section class="card card-front">
    <div class="sea-photo" role="img" aria-label="Photograph of moonlit ocean waves glittering under a night sky"></div>
    <div class="front-logo">harbourne vista</div>
    <div class="front-tagline">Audio Marine Ltd.</div>
  </section>

  <section class="card card-back">
    <div class="side-strip" role="img" aria-label="Black panel with white flowing swirl ornament"></div>
    <div class="side-logo">
      <span class="name">harbourne vista</span>
      <span class="sub">Audio Marine Ltd.</span>
    </div>

    <div class="person">
      <div class="person-name">Dale Penhallow</div>
      <div class="person-role">Managing Director</div>
    </div>

    <ul class="contact">
      <li class="company">Harbourne Vista Audio Marine Ltd</li>
      <li>Office: 01632 960482</li>
      <li>Mobile: 07700 900317</li>
      <li>dale@harbournevistaaudio.co.uk</li>
      <li>www.harbournevistaaudio.co.uk</li>
    </ul>
  </section>

</div>
</body>
</html>
```